New writer needs an ebook cover design

My book is a non-fiction travelogue where I travel around every brewery in Scotland in an old Dutch campervan called Gerald. The book is called 'The Copper Kettle Riddle' with the subtitle 'Chasing hops across the misty glens'. The image will need to work as a thumbprint as well as full-size. The key aspects of the book would be beer (craft beer, real ale etc, not corporate brands), Gerald and Scotland. The reader should feel that they are riding along with Gerald, discovering beer and Scotland as I make my way to remote locations and islands, visiting sixty breweries as we go. The book is not a technical guide or for reference purposes. Design must be suitable for Pellora Reader upload. Cheers!

Target Market(s)

Lovers of beer, travel, Scotland and campervans

Industry/Entity Type

Brewery

Requirements
Must have
• The title, subtitle and author's name - Douglas Farquhar. Also things that, directly or indirectly, convey some or all of beer, campervan and Scotland.
Nice to have
• A beermat or pumpclip with Gerald on it would be one suggestion for the central part of the image. An actual image of Gerald, be it real or cartooned could be used plus something to suggest Scotland.
Should not have
• Puns

```html
<!DOCTYPE html>
<html lang="en">
<head>
<meta charset="utf-8">
<title>The Copper Kettle Riddle — Douglas Farquhar</title>
<link rel="stylesheet" href="https://fonts.googleapis.com/css2?family=Montserrat:wght@700&family=Andada+Pro:wght@500&family=Delius&display=swap">
<style>
  :root {
    --page: #f2f2f2;
    --cover-blue: #1a6aad;
    --panel-navy: #0b3f8c;
    --cream: #eeeae0;
    --white: #ffffff;
    --bottle-dark: #0b4a1f;
    --bottle-mid: #1f5e25;
    --bottle-light: #2b6a2a;
  }
  * { margin: 0; padding: 0; box-sizing: border-box; }
  html, body { width: 1200px; height: 1000px; overflow: hidden; background: var(--page); }
  .canvas {
    width: 1200px; height: 1000px;
    display: flex; align-items: center; justify-content: center;
  }
  .cover {
    position: relative;
    width: 600px; height: 900px;
    background: var(--cover-blue);
    overflow: hidden;
    box-shadow: 0 6px 24px rgba(0,0,0,0.18);
  }
  .author {
    position: absolute; top: 52px; left: 0; right: 0;
    text-align: center;
    font-family: "Montserrat", sans-serif; font-weight: 700;
    font-size: 40px; letter-spacing: 1px;
    color: var(--white);
  }
  .title-panel {
    position: absolute; top: 140px; left: 135px;
    width: 330px; height: 330px;
  }
  .title-panel-fill { position: absolute; inset: 0; }
  .title {
    position: absolute; inset: 0;
    display: flex; flex-direction: column; align-items: center; justify-content: center;
    font-family: "Andada Pro", serif; font-weight: 500;
    color: var(--cream);
    line-height: 1.05; text-align: center;
  }
  .title-line { display: block; font-size: 50px; }
  .title-line--wide { font-size: 40px; }
  .subtitle {
    position: absolute; top: 510px; left: 70px;
    font-family: "Delius", cursive;
    color: var(--cream);
    transform: rotate(-4deg);
    transform-origin: left top;
  }
  .subtitle-main { display: block; font-size: 52px; line-height: 1.05; }
  .subtitle-rest { display: block; font-size: 30px; margin-left: 40px; }
  .bottles {
    position: absolute; left: 0; bottom: 0;
    width: 600px; height: 380px;
  }
</style>
</head>
<body>
<main class="canvas">
  <section class="cover">
    <p class="author">Douglas Farquhar</p>

    <div class="title-panel">
      <svg class="title-panel-fill" viewBox="0 0 330 330" width="330" height="330" role="img" aria-label="Plain panel behind the book title">
        <rect x="0" y="0" width="330" height="330" rx="24" fill="var(--panel-navy)"/>
      </svg>
      <h1 class="title">
        <span class="title-line">The</span>
        <span class="title-line title-line--wide">Copper Kettle</span>
        <span class="title-line">Riddle</span>
      </h1>
    </div>

    <p class="subtitle">
      <span class="subtitle-main">Chasing hops</span>
      <span class="subtitle-rest">across the misty glens</span>
    </p>

    <svg class="bottles" viewBox="0 0 600 380" role="img" aria-label="Row of green beer bottle silhouettes along the bottom of the cover">
      <defs>
        <linearGradient id="bottleFill" x1="0" y1="0" x2="1" y2="0">
          <stop offset="0" stop-color="var(--bottle-light)"/>
          <stop offset="0.5" stop-color="var(--bottle-mid)"/>
          <stop offset="1" stop-color="var(--bottle-dark)"/>
        </linearGradient>
      </defs>
      <path d="M0 250 L120 220 L260 180 L400 110 L520 60 L600 30 L600 380 L0 380 Z" fill="url(#bottleFill)"/>
    </svg>
  </section>
</main>
</body>
</html>
```